Breast Cancer Stickers

Hi,
i would like a of small design for a breast cancer awareness campaign. please check attached picture this is the size and font i want. these will be stickers. Then i would like a little pink ribbon after each dot. so there will be four design please find below colors, slogans, etc..
1 I PINK I CAN. (Off white Background, Light Pink Font)
Never give up.
2 PINK POWER. (Black Background, Bright Pink Font)
Theres Always hope
3 POSITIVELY PINK. ( Light Pink Background, Off white Font)
Stay Positive
4 TURN UP THE PINK. (Bright Pink Background, Black font)
fight on.
Campaign

```html
<!DOCTYPE html>
<html lang="en">
<head>
<meta charset="UTF-8">
<title>Stay Positive – Awareness Sticker</title>
<link href="https://fonts.googleapis.com/css2?family=Arimo:wght@700&display=swap" rel="stylesheet">
<style>
  :root {
    --sticker-pink: #ff5c8f;
    --sticker-white: #ffffff;
  }
  html, body {
    margin: 0;
    padding: 0;
    width: 1200px;
    height: 934px;
    overflow: hidden;
    background: var(--sticker-pink);
  }
  .sticker {
    position: relative;
    width: 1200px;
    height: 934px;
    background: var(--sticker-pink);
    overflow: hidden;
  }
  .slogan {
    margin: 0;
    font-family: "Arimo", Arial, sans-serif;
    font-weight: 700;
    font-size: 220px;
    line-height: 1;
    color: var(--sticker-white);
    letter-spacing: -2px;
  }
  .slogan-line {
    position: absolute;
    left: 93px;
    white-space: nowrap;
  }
  .slogan-line--first { top: 217px; }
  .slogan-line--second { top: 418px; }
  .awareness-ribbon {
    position: absolute;
    left: 1010px;
    top: 482px;
    width: 96px;
    height: 140px;
  }
  .awareness-ribbon path {
    fill: none;
    stroke: var(--sticker-white);
    stroke-width: 14;
    stroke-linejoin: round;
  }
</style>
</head>
<body>
  <main class="sticker">
    <h1 class="slogan">
      <span class="slogan-line slogan-line--first">Stay</span>
      <span class="slogan-line slogan-line--second">Positive.</span>
    </h1>
    <svg class="awareness-ribbon" viewBox="0 0 96 140" aria-hidden="true">
      <path d="M12,130 L52,72 C66,52 72,40 70,28 C68,16 58,10 48,10 C38,10 28,16 26,28 C24,40 30,52 44,72 L84,130"/>
    </svg>
  </main>
</body>
</html>
```